Re-branding for Structural Engineering firm

We need new business cards as part of our current re-branding. We have a new logo (attached), so the card design should incorporate this color scheme. We are a structural engineering firm providing structural building design and seismic consulting services. The final design should communicate professionalism and stability, with a modern look and feel.

```html
<!DOCTYPE html>
<html lang="en">
<head>
<meta charset="utf-8">
<title>Halden Structural Engineering – Business Card</title>
<link href="https://fonts.googleapis.com/css2?family=Roboto:wght@400;500&display=swap" rel="stylesheet">
<style>
  :root {
    --stage: #1c1c1e;
    --card-dark: #111112;
    --card-light: #ffffff;
    --brand-blue: #1f76c0;
    --brand-grey: #808285;
    --ink: #121212;
    --text-grey: #58595b;
  }
  * { margin: 0; padding: 0; box-sizing: border-box; }
  html, body {
    width: 1200px; height: 1200px; overflow: hidden;
    background: var(--stage);
    font-family: "Roboto", Arial, sans-serif;
  }
  .card {
    position: absolute; left: 150px;
    width: 900px; height: 514px;
    box-shadow: 0 12px 30px rgba(0,0,0,.5);
  }
  .card-back { top: 50px; background: var(--card-dark); }
  .card-front { top: 624px; background: var(--card-light); }

  .brand {
    position: absolute; display: flex; align-items: center; gap: 16px;
  }
  .brand-square { background: var(--brand-blue); flex: none; }
  .brand-name {
    font-weight: 500; text-transform: uppercase; line-height: 1.12;
    letter-spacing: .5px;
  }
  .card-back .brand { left: 50%; top: 50%; transform: translate(-50%, -50%); }
  .card-back .brand-square { width: 70px; height: 70px; }
  .card-back .brand-name { color: var(--brand-grey); font-size: 26px; }

  .card-front .brand { left: 70px; top: 170px; flex-direction: column; align-items: flex-start; gap: 18px; }
  .card-front .brand-square { width: 110px; height: 110px; }
  .card-front .brand-name { color: var(--brand-blue); font-size: 27px; }

  .divider {
    position: absolute; left: 350px; top: 120px;
    width: 2px; height: 270px; background: var(--brand-grey);
  }
  .details { position: absolute; left: 382px; top: 118px; }
  .person-name { font-size: 31px; font-weight: 500; color: var(--ink); letter-spacing: 1px; }
  .person-title { font-size: 19px; font-weight: 500; color: var(--brand-blue); letter-spacing: 1px; margin-top: 2px; }
  .contacts { list-style: none; margin-top: 22px; }
  .contacts li {
    display: flex; align-items: center; gap: 12px;
    font-size: 20px; color: var(--text-grey); letter-spacing: 1px; height: 30px;
  }
  .contacts svg { width: 18px; height: 18px; fill: var(--brand-blue); flex: none; }
  .address { margin-top: 18px; font-size: 20px; color: var(--text-grey); letter-spacing: 1px; line-height: 1.3; }

  .bar { position: absolute; left: 715px; width: 36px; }
  .bar-blue { top: 0; height: 300px; background: var(--brand-blue); }
  .bar-grey { top: 312px; height: 202px; background: var(--brand-grey); }
</style>
</head>
<body>
  <section class="card card-back" aria-label="Card back">
    <div class="brand">
      <span class="brand-square"></span>
      <span class="brand-name">Halden<br>Structural<br>Engineering</span>
    </div>
  </section>

  <section class="card card-front" aria-label="Card front">
    <div class="brand">
      <span class="brand-square"></span>
      <span class="brand-name">Halden<br>Structural<br>Engineering</span>
    </div>
    <div class="divider"></div>
    <div class="details">
      <h1 class="person-name">DANA WHITLOW, S.E.</h1>
      <p class="person-title">PRINCIPAL</p>
      <ul class="contacts">
        <li><svg viewBox="0 0 24 24" aria-hidden="true"><path d="M3 8c0-3 4-5 9-5s9 2 9 5v2h-5V8H8v2H3zM6 12h12l3 9H3z"/></svg>555.214.3080</li>
        <li><svg viewBox="0 0 24 24" aria-hidden="true"><path d="M6 2h12a2 2 0 0 1 2 2v16a2 2 0 0 1-2 2H6a2 2 0 0 1-2-2V4a2 2 0 0 1 2-2zm0 3v13h12V5z"/></svg>555.731.9462</li>
        <li><svg viewBox="0 0 24 24" aria-hidden="true"><path d="M2 5h20v14H2zm2 2v.5l8 6 8-6V7zm0 3v7h16v-7l-8 6z"/></svg>dana@haldense.com</li>
        <li><svg viewBox="0 0 24 24" aria-hidden="true"><path d="M12 2a10 10 0 1 0 0 20 10 10 0 0 0 0-20zm0 2c1 0 2.5 2.5 2.9 7H9.1C9.5 6.5 11 4 12 4zM4.1 11a8 8 0 0 1 3.5-5.7C7.3 7 7.1 9 7.1 11zm0 2h3c0 2 .2 4 .5 5.7A8 8 0 0 1 4.1 13zm5 0h5.8c-.4 4.5-1.9 7-2.9 7s-2.5-2.5-2.9-7zm7.8 0h3a8 8 0 0 1-3.5 5.7c.3-1.7.5-3.7.5-5.7zm0-2c0-2-.2-4-.5-5.7a8 8 0 0 1 3.5 5.7z"/></svg>www.haldense.com</li>
      </ul>
      <p class="address">4170 Cedar Ridge Ave., Ste 210<br>Harbor City, CA 90000</p>
    </div>
    <div class="bar bar-blue"></div>
    <div class="bar bar-grey"></div>
  </section>
</body>
</html>
```